make a fireworks website

we are manufacturer of fireworks in Asia.
we need a HD fireworks website for showing product to all world customers.
we also need an register for member system,location, forum,products..etc
I added my Logo for the company.
brightnova.com.hk

and please message me if you have
any question.
here some example of website:
http://www.skyplumeshow.com/
http://www.tornelupyro.com/
http://www.quarvel-pyro.co.uk/
http://www.mirethpyro.co.uk/

```html
<!DOCTYPE html>
<html lang="en">
<head>
<meta charset="utf-8">
<title>BrightNova Fireworks</title>
<link href="https://fonts.googleapis.com/css2?family=Open+Sans:wght@400;600;700;800&display=swap" rel="stylesheet">
<style>
:root{
  --pink:#e8267a;
  --pink-soft:#ea3f80;
  --orange:#f6b637;
  --ink:#1b1b1b;
  --night:#141414;
  --grey:#6d6d6d;
  --white:#ffffff;
}
*{margin:0;padding:0;box-sizing:border-box}
html,body{width:714px;height:1200px;overflow:hidden;background:var(--white)}
body{font-family:"Open Sans",Arial,sans-serif;color:var(--ink);font-size:9px}
.page{width:714px;height:1200px;position:relative;overflow:hidden}

/* hero */
.hero{position:relative;height:278px;background:radial-gradient(ellipse at 55% 38%,#d2357f 0%,#7a1f5a 22%,#2b0f2d 52%,#0b0710 85%)}
.hero-photo{position:absolute;inset:0}
.topbar{position:absolute;top:0;left:0;right:0;height:26px;display:flex;justify-content:flex-end;padding-right:40px}
.nav{display:flex;list-style:none}
.nav li{width:58px;height:26px;line-height:26px;text-align:center;color:var(--white);font-size:7px;font-weight:600;letter-spacing:.5px}
.nav li.active{background:var(--pink)}
.nav li.cart{width:30px;display:flex;align-items:center;justify-content:center}
.brand{position:absolute;left:24px;top:34px;display:flex;align-items:center;gap:10px}
.brand-dot{width:34px;height:34px;border-radius:50%;background:var(--pink)}
.brand-name{color:var(--white);font-weight:800;font-size:30px;letter-spacing:-.5px}
.hero-text{position:absolute;left:0;right:0;top:166px;text-align:center;color:var(--white);font-size:11px;line-height:15px}

.quicklinks{display:flex;justify-content:center;gap:4px;margin-top:4px}
.quicklinks a{display:block;width:172px;height:22px;line-height:22px;background:var(--pink);color:var(--white);text-align:center;font-size:8px;font-weight:600;text-decoration:none;letter-spacing:.5px}

/* best selling */
.best-title{text-align:center;font-size:17px;margin-top:16px;font-weight:400}
.best-title strong{color:var(--pink);font-weight:700}
.sub{text-align:center;font-size:7px;color:var(--grey);margin-top:2px}
.strip{margin-top:10px;height:90px;background:var(--night);display:flex;justify-content:center;gap:22px;padding-top:8px}
.strip-item{width:96px;text-align:center}
.strip-photo{height:58px;background:linear-gradient(160deg,#5a2c6e,#2a1a2a 60%,#1a1a1a)}
.strip-item:nth-child(2) .strip-photo{background:linear-gradient(160deg,#d7a53a,#8a2a6e 55%,#2a1a2a)}
.strip-item:nth-child(3) .strip-photo{background:linear-gradient(160deg,#3b5ea8,#2a2a40 60%,#1a1a1a)}
.strip-item:nth-child(4) .strip-photo{background:linear-gradient(160deg,#6e6e6e,#2f2f2f 60%,#1a1a1a)}
.strip-item:nth-child(5) .strip-photo{background:linear-gradient(160deg,#b8473a,#3a2020 60%,#1a1a1a)}
.strip-name{color:var(--white);font-size:7px;margin-top:4px;height:13px;line-height:13px}
.strip-item.selected .strip-name{background:var(--pink);font-weight:700}

/* offers */
.offers{position:relative;height:253px}
.offers-tab{position:absolute;left:50%;top:8px;transform:translateX(-50%);background:var(--pink);color:var(--white);font-size:16px;font-weight:700;padding:3px 40px;border-radius:3px;white-space:nowrap}
.offers-tab span{margin:0 6px}
.offers-row{display:flex;justify-content:center;gap:32px;padding-top:92px}
.offer{width:92px;text-align:center}
.offer-photo{height:80px;background:linear-gradient(180deg,#f7d9e6,#e7a3c0 60%,#ffffff)}
.offer:nth-child(2) .offer-photo{background:linear-gradient(180deg,#fde7b8,#e8b34a 60%,#fff)}
.offer:nth-child(3) .offer-photo{background:linear-gradient(180deg,#f8c8c8,#d04a4a 60%,#fff)}
.offer:nth-child(4) .offer-photo{background:linear-gradient(180deg,#e1e1e1,#9a9a9a 60%,#fff)}
.offer:nth-child(5) .offer-photo{background:linear-gradient(180deg,#f4d2b0,#b35a2e 60%,#fff)}
.price{margin-top:5px;font-size:8px}
.price .now{color:var(--pink);font-weight:700;margin-right:6px}
.price .was{color:var(--grey);text-decoration:line-through}
.offer p{font-size:6.5px;color:var(--grey);line-height:9px;margin-top:3px}

/* videos */
.videos{background:var(--ink);height:226px;padding-top:16px;text-align:center;color:var(--white)}
.videos h2{font-size:15px;font-weight:400}
.videos h2 strong{color:var(--pink);font-weight:700}
.videos .sub{color:#bdbdbd}
.video-row{display:flex;justify-content:center;gap:10px;margin-top:12px}
.video{width:196px}
.video-photo{height:128px;position:relative;background:radial-gradient(circle at 50% 45%,#c9902c 0%,#6a3a1a 30%,#1c130e 65%,#0d0d0d)}
.video:nth-child(2) .video-photo{background:radial-gradient(circle at 50% 45%,#b86a8a 0%,#4a2a3a 35%,#151015 70%)}
.play{position:absolute;left:50%;top:50%;transform:translate(-50%,-50%)}
.video-cap{font-size:6.5px;color:#bdbdbd;margin-top:5px}

/* info boxes */
.info{display:flex;justify-content:center;gap:14px;margin-top:14px}
.info-box{width:296px;height:148px;padding:14px 16px;color:var(--white)}
.info-box.pink{background:var(--pink-soft)}
.info-box.orange{background:var(--orange)}
.info-box h3{font-size:10px;font-weight:700;margin-bottom:6px}
.info-box p{font-size:7px;line-height:11px}

/* footer */
.footer{position:absolute;left:0;right:0;bottom:0;height:86px;background:var(--night);display:flex;gap:30px;padding:10px 0 0 92px;color:#cfcfcf;font-size:6px;line-height:8px}
.footer h4{color:var(--white);font-size:7px;font-weight:700;margin-bottom:3px}
.footer ul{list-style:none}
.pay{display:flex;gap:4px;margin-top:4px}
.pay i{display:block;width:22px;height:13px;background:#3d3d3d;border-radius:2px}
.social{display:grid;grid-template-columns:repeat(2,46px);gap:4px}
.social i{display:block;height:12px;border-radius:2px}
.social i:nth-child(1){background:#3b5998}
.social i:nth-child(2){background:#2aa9e0}
.social i:nth-child(3){background:var(--pink)}
.social i:nth-child(4){background:#4a4a4a}
</style>
</head>
<body>
<div class="page">

  <header class="hero">
    <div class="hero-photo" role="img" aria-label="Harbour bridge at night under bursts of pink and white fireworks"></div>
    <div class="topbar">
      <ul class="nav">
        <li class="active">HOME</li><li>GALLERY</li><li>VIDEOS</li><li>NEWS</li><li>FORUM</li><li>MEMBER</li><li>CONTACT US</li>
        <li class="cart"><svg width="12" height="11" viewBox="0 0 12 11"><path d="M0 1h2l2 6h6l1.5-4.5H3" fill="none" stroke="#e8267a" stroke-width="1.3"/><circle cx="5" cy="9.5" r="1" fill="#e8267a"/><circle cx="9" cy="9.5" r="1" fill="#e8267a"/></svg></li>
      </ul>
    </div>
    <div class="brand"><span class="brand-dot"></span><span class="brand-name">BrightNova</span></div>
    <p class="hero-text">Lorem ipsum dolor sit amet, consectetur adipiscing elit. Donec vehicula magna ac nisi<br>imperdiet a suscipit nisi bibendum.</p>
  </header>

  <nav class="quicklinks">
    <a href="#">WHAT IS NEW?</a><a href="#">ALL PRODUCTS</a><a href="#">YOUR ACCOUNT</a>
  </nav>

  <section class="best">
    <h2 class="best-title">The <strong>BEST SELLING</strong> fireworks!</h2>
    <p class="sub">Lorem ipsum dolor sit amet, consectetur adipiscing elit. Donec vehicula magna ac nisi imperdiet a suscipit nisi bibendum.</p>
    <div class="strip">
      <div class="strip-item"><div class="strip-photo" role="img" aria-label="Lunar Stride firework cake box"></div><div class="strip-name">Lunar Stride</div></div>
      <div class="strip-item selected"><div class="strip-photo" role="img" aria-label="Violet Cascade firework cake box"></div><div class="strip-name">Violet Cascade</div></div>
      <div class="strip-item"><div class="strip-photo" role="img" aria-label="Starling firework cake box"></div><div class="strip-name">Starling</div></div>
      <div class="strip-item"><div class="strip-photo" role="img" aria-label="NV 4150 firework cake box"></div><div class="strip-name">NV 4150</div></div>
      <div class="strip-item"><div class="strip-photo" role="img" aria-label="Thunder Bloom firework cake box"></div><div class="strip-name">Thunder Bloom</div></div>
    </div>
  </section>

  <section class="offers">
    <div class="offers-tab"><span>Special</span><span>Offers</span></div>
    <div class="offers-row">
      <div class="offer"><div class="offer-photo" role="img" aria-label="Set of fountain fireworks"></div><div class="price"><span class="now">£4.00</span><span class="was">£6.00</span></div><p>Lorem ipsum dolor sit amet, consectetur</p></div>
      <div class="offer"><div class="offer-photo" role="img" aria-label="Pack of rockets"></div><div class="price"><span class="now">£4.00</span><span class="was">£6.00</span></div><p>Lorem ipsum dolor sit amet, consectetur</p></div>
      <div class="offer"><div class="offer-photo" role="img" aria-label="Pair of large rockets"></div><div class="price"><span class="now">£4.00</span><span class="was">£6.00</span></div><p>Lorem ipsum dolor sit amet, consectetur</p></div>
      <div class="offer"><div class="offer-photo" role="img" aria-label="Firework cake box"></div><div class="price"><span class="now">£4.00</span><span class="was">£6.00</span></div><p>Lorem ipsum dolor sit amet, consectetur</p></div>
      <div class="offer"><div class="offer-photo" role="img" aria-label="Selection box of fireworks"></div><div class="price"><span class="now">£4.00</span><span class="was">£6.00</span></div><p>Lorem ipsum dolor sit amet, consectetur</p></div>
    </div>
  </section>

  <section class="videos">
    <h2>See the <strong>MOST BEUTIFUL FIREWORKS!</strong></h2>
    <p class="sub">Lorem ipsum dolor sit amet, consectetur adipiscing elit. Donec vehicula magna ac nisi imperdiet a suscipit nisi bibendum.</p>
    <div class="video-row">
      <div class="video"><div class="video-photo" role="img" aria-label="Golden firework burst video still"></div><div class="video-cap">Suscipit nisi bibendum</div></div>
      <div class="video"><div class="video-photo" role="img" aria-label="Pink firework display video still"><svg class="play" width="22" height="22" viewBox="0 0 22 22"><circle cx="11" cy="11" r="10" fill="rgba(0,0,0,.5)" stroke="#fff" stroke-width="1.2"/><path d="M9 6.5l6 4.5-6 4.5z" fill="#fff"/></svg></div><div class="video-cap">Suscipit nisi bibendum</div></div>
      <div class="video"><div class="video-photo" role="img" aria-label="Golden firework burst video still"></div><div class="video-cap">Suscipit nisi bibendum</div></div>
    </div>
  </section>

  <section class="info">
    <div class="info-box pink"><h3>Lorem ipsum dolor</h3><p>Lorem ipsum dolor sit amet, consectetur adipiscing elit. Donec vehicula magna ac nisi imperdiet a suscipit nisi bibendum. Lorem ipsum dolor sit amet, consectetur adipiscing elit. Donec vehicula magna ac nisi imperdiet a suscipit nisi bibendum. Lorem ipsum dolor sit amet, consectetur adipiscing elit.</p></div>
    <div class="info-box orange"><h3>Lorem ipsum dolor</h3><p>Lorem ipsum dolor sit amet, consectetur adipiscing elit. Donec vehicula magna ac nisi imperdiet a suscipit nisi bibendum. Lorem ipsum dolor sit amet, consectetur adipiscing elit. Donec vehicula magna ac nisi imperdiet a suscipit nisi bibendum. Lorem ipsum dolor sit amet, consectetur adipiscing elit.</p></div>
  </section>

  <footer class="footer">
    <div><h4>Home</h4><ul><li>Gallery</li><li>Videos</li><li>News</li><li>Forum</li><li>Member</li><li>Contact Us</li></ul></div>
    <div><h4>We accept these payment methods</h4><div class="pay"><i></i><i></i><i></i><i></i></div></div>
    <div><h4>Contacts</h4><ul><li>E-mail: sales@brightnova.com.hk</li><li>Phone: 000 000 0000</li><li>Address: 18 Lumen Lane</li><li>Starport</li></ul></div>
    <div><h4>Follow Us</h4><div class="social"><i></i><i></i><i></i><i></i></div></div>
  </footer>

</div>
</body>
</html>
```